Hi,
Brackwell Construction is a domestic builder on the Gold Coast specializing in new homes, townhouses, duplexes and high end renovations.
Brackwell Construction can make your dream new home or development a reality. Whether you already have plans or require a complete design and construct project service, Brackwell Construction will make your project a stress free experience.
We offer design, town planning, certification and construction services.

Target Market(s)

Anyone looking to build.

Industry/Entity Type

Building

Coding

Coded - Design and coding required

Font styles to use
Other font styles liked:
• Match logo

Colors

Designer to choose colors to be used in the design.

Requirements
Must have
• Attractive home page with logo etc.
• About us page
• Gallery page
• Services Page
• Contact us page

```html
<!DOCTYPE html>
<html lang="en">
<head>
<meta charset="utf-8">
<title>Brackwell Construction</title>
<link href="https://fonts.googleapis.com/css2?family=Mulish:wght@400;600;700&display=swap" rel="stylesheet">
<style>
:root{
  --gold:#d9b33a;
  --navy:#1d2433;
  --text:#5d6270;
  --muted:#8a8f99;
  --card:#f3f4f8;
  --white:#ffffff;
  --footer:#f1f1f1;
}
*{box-sizing:border-box;margin:0;padding:0}
html,body{width:1200px;height:3261px;overflow:hidden;background:var(--white)}
body{font-family:"Mulish",sans-serif;color:var(--navy);position:relative}
.abs{position:absolute}

/* hero */
.hero{left:0;top:0;width:1200px;height:560px;background:linear-gradient(180deg,#1c2b45 0%,#3a4458 45%,#4a4036 75%,#2a2a22 100%)}
.hero-shade{left:0;top:0;width:1200px;height:560px;background:linear-gradient(90deg,rgba(10,16,28,.55) 0%,rgba(10,16,28,.1) 60%)}
.brand{left:156px;top:40px;display:flex;align-items:center;gap:12px}
.brand-mark{width:44px;height:44px;border:2px solid var(--white);border-radius:50%}
.brand-name{color:var(--white);font-size:26px;font-weight:400}
.nav{top:66px;display:flex;font-size:11px;font-weight:700;letter-spacing:.5px;color:var(--white)}
.nav a{position:absolute;white-space:nowrap;color:var(--white);text-decoration:none}
.nav a.active{color:var(--gold)}
.phone-top{left:808px;top:64px;color:var(--gold);font-size:13px;font-weight:600;display:flex;align-items:center;gap:6px}
.social-top span{position:absolute;top:66px;width:12px;height:12px;border:1.5px solid var(--white);border-radius:2px}
.hero-title{left:156px;top:228px;font-size:38px;font-weight:600;color:var(--white)}
.hero-sub{left:156px;top:296px;width:440px;font-size:22px;line-height:28px;color:var(--white)}
.btn-gold{background:var(--gold);color:var(--white);font-size:11px;font-weight:700;letter-spacing:1px;display:flex;align-items:center;justify-content:center}
.hero-btn{left:156px;top:386px;width:144px;height:30px}
.circle-arrow{width:30px;height:30px;border:1.5px solid var(--white);border-radius:50%}
.dot{left:1031px;width:12px;height:12px;border:1.5px solid var(--white);border-radius:50%}

/* about */
.about-photo{left:156px;top:639px;width:368px;height:400px;background:linear-gradient(180deg,#dfe6ee 0%,#b9a98a 45%,#5f8a3c 75%,#c9c9c4 100%)}
.years-frame{left:461px;top:724px;width:126px;height:200px;border:3px solid var(--gold)}
.years-num{left:478px;top:798px;font-size:72px;font-weight:700;color:var(--navy);line-height:1}
.years-word{left:481px;top:882px;font-size:30px;font-weight:700;color:var(--navy);line-height:1}
.years-sub{left:481px;top:925px;font-size:14px;color:var(--navy)}
.eyebrow{color:var(--gold);font-size:14px;font-weight:600}
.about-eyebrow{left:687px;top:678px}
.about-title{left:687px;top:716px;width:400px;font-size:28px;line-height:35px;font-weight:600}
.body-text{font-size:12px;line-height:18px;color:var(--text)}
.about-text{left:687px;top:846px;width:360px}
.btn-outline{border:1.5px solid var(--gold);color:var(--gold);font-size:11px;font-weight:700;letter-spacing:1px;display:flex;align-items:center;justify-content:center}
.about-btn{left:687px;top:965px;width:146px;height:31px}

/* services */
.services-eyebrow{left:156px;top:1117px}
.service{top:1166px;width:270px}
.service-icon{width:70px;height:68px}
.service h3{margin-top:28px;font-size:23px;font-weight:600}
.service p{margin-top:14px}
.read-more{display:block;margin-top:16px;font-size:10px;font-weight:700;letter-spacing:1px;color:var(--gold)}

/* projects */
.projects-title{left:156px;top:1497px;font-size:27px;font-weight:600}
.pager{top:1498px;width:32px;height:32px;border-radius:50%;border:1.5px solid var(--gold)}
.pager.filled{background:var(--gold)}
.project{top:1563px;width:272px;height:320px}
.project-1{left:24px;background:linear-gradient(180deg,#7fa4cc 0%,#3d4b6a 45%,#8a8d8f 100%)}
.project-2{left:317px;background:linear-gradient(180deg,#c8a63a,#b8952b)}
.project-3{left:611px;background:linear-gradient(180deg,#4f8fd8 0%,#5d6b80 50%,#7ea34a 100%)}
.project-4{left:904px;background:linear-gradient(135deg,#c9c1b4 0%,#6b5145 55%,#3b2a22 100%)}
.project-caption{left:317px;top:1678px;width:272px;text-align:center;color:var(--white);font-size:17px;line-height:24px}
.view-btn{left:537px;top:1915px;width:126px;height:31px}

/* testimonials */
.testi-eyebrow{left:0;top:2026px;width:1200px;text-align:center;font-size:13px}
.testi-title{left:0;top:2047px;width:1200px;text-align:center;font-size:29px;font-weight:600}
.testi-card{top:2141px;width:432px;height:224px;background:var(--card);padding:50px 30px 0 30px}
.quote-badge{top:2116px;width:48px;height:48px;border-radius:50%;border:2px solid var(--gold);background:var(--white);display:flex;align-items:center;justify-content:center;color:var(--gold);font-size:34px;font-weight:700;line-height:1}
.testi-name{margin-top:22px;color:var(--gold);font-size:15px;font-weight:700}
.testi-role{margin-top:4px;font-size:12px;color:var(--text)}

/* contact */
.contact{left:0;top:2444px;width:1200px;height:417px;background:linear-gradient(180deg,#242b2a 0%,#3f3a2e 45%,#6b5530 70%,#2e2b24 100%)}
.contact-title{left:0;top:2514px;width:1200px;text-align:center;color:var(--white);font-size:28px;font-weight:600}
.contact-sub{left:0;top:2556px;width:1200px;text-align:center;color:var(--white);font-size:12px}
.field{left:233px;width:358px;height:33px;background:var(--white);border-radius:2px;font-size:11px;color:var(--muted);padding:9px 12px}
.field-msg{left:609px;top:2600px;width:356px;height:126px}
.send-btn{left:554px;top:2752px;width:94px;height:31px}

/* footer */
.footer{left:0;top:2861px;width:1200px;height:400px;background:var(--footer)}
.footer-mark{left:570px;top:2939px;width:60px;height:60px;border:2px solid var(--navy);border-radius:50%}
.footer-name{left:0;top:3010px;width:1200px;text-align:center;font-size:24px;color:var(--navy)}
.footer-call{left:0;top:3077px;width:1200px;text-align:center;font-size:16px;color:var(--navy)}
.footer-call b{color:var(--gold);font-weight:400}
.f-social{top:3119px;width:38px;height:38px;border-radius:50%;border:1.5px solid var(--gold)}
.f-social.filled{background:var(--gold)}
.f-social i{position:absolute;left:12px;top:12px;width:12px;height:12px;border:1.5px solid var(--gold);border-radius:2px}
.f-social.filled i{border-color:var(--white)}
.copyright{left:0;top:3180px;width:1200px;text-align:center;font-size:10px;letter-spacing:.5px;color:var(--text)}
.legal{left:0;top:3199px;width:1200px;text-align:center;font-size:10px;color:var(--text)}
</style>
</head>
<body>

<section class="abs hero" role="img" aria-label="Photo of a large two-storey house with a lit terrace at dusk"></section>
<div class="abs hero-shade"></div>
<div class="abs brand"><span class="brand-mark"></span><span class="brand-name">Brackwell</span></div>
<nav class="abs nav">
  <a class="active" style="left:359px">HOME</a>
  <a style="left:424px">ABOUT US</a>
  <a style="left:511px">SERVICES</a>
  <a style="left:598px">GALLERY</a>
  <a style="left:680px">CONTACT US</a>
</nav>
<div class="abs phone-top">
  <svg width="12" height="12" viewBox="0 0 24 24"><path d="M6.6 10.8a15 15 0 0 0 6.6 6.6l2.2-2.2a1 1 0 0 1 1-.25 11.4 11.4 0 0 0 3.6.57 1 1 0 0 1 1 1V20a1 1 0 0 1-1 1A17 17 0 0 1 3 4a1 1 0 0 1 1-1h3.5a1 1 0 0 1 1 1c0 1.25.2 2.45.57 3.6a1 1 0 0 1-.25 1z" fill="#d9b33a"/></svg>
  555-204-7731
</div>
<div class="social-top">
  <span style="left:957px"></span><span style="left:983px;border-color:var(--gold)"></span><span style="left:1010px"></span><span style="left:1033px"></span>
</div>
<h1 class="abs hero-title">We Build Your Dream</h1>
<p class="abs hero-sub">We know that good design means good business</p>
<div class="abs btn-gold hero-btn">EXPLORE MORE</div>
<div class="abs circle-arrow" style="left:155px;top:498px"><svg width="27" height="27" viewBox="0 0 27 27"><path d="M15 9l-5 4.5 5 4.5" stroke="#fff" stroke-width="1.5" fill="none"/></svg></div>
<div class="abs circle-arrow" style="left:196px;top:498px"><svg width="27" height="27" viewBox="0 0 27 27"><path d="M12 9l5 4.5-5 4.5" stroke="#fff" stroke-width="1.5" fill="none"/></svg></div>
<span class="abs dot" style="top:303px"></span>
<span class="abs dot" style="top:320px"></span>
<span class="abs dot" style="top:337px"></span>

<div class="abs about-photo" role="img" aria-label="Photo of a suburban family home with a landscaped front garden"></div>
<div class="abs years-frame"></div>
<div class="abs years-num">30</div>
<div class="abs years-word">YEARS</div>
<div class="abs years-sub">Working</div>
<p class="abs eyebrow about-eyebrow">Brackwell Construction</p>
<h2 class="abs about-title">There are Many Variations of Passages Lorem Ipsum</h2>
<p class="abs body-text about-text">Contrary to popular belief, Lorem Ipsum is not simply random text. It has roots in a piece of classical Latin literature from 45 BC, making it over 2000 years old. Alden Marsh, a Latin professor at Harlow Ridge College in Virginia, looked ...</p>
<div class="abs btn-outline about-btn">DISCOVER MORE</div>

<p class="abs eyebrow services-eyebrow">Our Services</p>
<div class="abs service" style="left:159px">
  <svg class="service-icon" viewBox="0 0 70 68" fill="none" stroke="#1d2433" stroke-width="2.5"><path d="M4 64h62M10 64V34l16-14 16 14v30M42 40h18v24M18 64V48h16v16M14 20V6h8v9"/><circle cx="30" cy="8" r="4"/><circle cx="38" cy="4" r="3"/></svg>
  <h3>New Homes</h3>
  <p class="body-text">Contrary to popular belief, Lorem Ipsum is not simply random text. It has an roots roots in a piece of classical Latin literature from 45 ...</p>
  <span class="read-more">READ MORE</span>
</div>
<div class="abs service" style="left:463px">
  <svg class="service-icon" viewBox="0 0 70 68" fill="none" stroke="#d9b33a" stroke-width="2.5"><path d="M4 64h62M10 64V32L35 10l25 22v32M4 36l31-28 31 28M18 64V46h12v18M38 44h14v10H38zM28 30h14"/></svg>
  <h3>Renovations</h3>
  <p class="body-text">Contrary to popular belief, Lorem Ipsum is not simply random text. It has an roots roots in a piece of classical Latin literature from 45 ...</p>
  <span class="read-more">READ MORE</span>
</div>
<div class="abs service" style="left:767px">
  <svg class="service-icon" viewBox="0 0 70 68" fill="none" stroke="#1d2433" stroke-width="2.5"><path d="M4 64h62M8 64V24h16v40M24 64V8h22v56M46 64V24h16v40M30 16h4M36 16h4M30 26h4M36 26h4M30 36h4M36 36h4M13 34h6M13 44h6M51 34h6M51 44h6M31 64V52h8v12"/></svg>
  <h3>Town Houses</h3>
  <p class="body-text">Contrary to popular belief, Lorem Ipsum is not simply random text. It has an roots roots in a piece of classical Latin literature from 45 ...</p>
  <span class="read-more">READ MORE</span>
</div>

<h2 class="abs projects-title">Latest Projects</h2>
<div class="abs pager" style="left:973px"><svg width="29" height="29" viewBox="0 0 29 29"><path d="M16 10l-4 4.5 4 4.5" stroke="#d9b33a" stroke-width="1.5" fill="none"/></svg></div>
<div class="abs pager filled" style="left:1012px"><svg width="29" height="29" viewBox="0 0 29 29"><path d="M13 10l4 4.5-4 4.5" stroke="#fff" stroke-width="1.5" fill="none"/></svg></div>
<div class="abs project project-1" role="img" aria-label="Photo of a modern two-storey home with a double garage"></div>
<div class="abs project project-2" role="img" aria-label="Photo of a private residence under a gold overlay"></div>
<p class="abs project-caption">Private Residence<br>New Yourk</p>
<div class="abs project project-3" role="img" aria-label="Photo of a grey suburban house under blue sky"></div>
<div class="abs project project-4" role="img" aria-label="Photo of a modern living room interior"></div>
<div class="abs btn-outline view-btn">VIEW ALL</div>

<p class="abs eyebrow testi-eyebrow">Testimonials</p>
<h2 class="abs testi-title">What Our Clients Are Saying</h2>
<svg class="abs" style="left:120px;top:2244px" width="12" height="16" viewBox="0 0 12 16"><path d="M10 1L2 8l8 7" stroke="#1d2433" stroke-width="1.5" fill="none"/></svg>
<svg class="abs" style="left:1068px;top:2244px" width="12" height="16" viewBox="0 0 12 16"><path d="M2 1l8 7-8 7" stroke="#d9b33a" stroke-width="1.5" fill="none"/></svg>
<article class="abs testi-card" style="left:156px">
  <p class="body-text">Contrary to popular belief, Lorem Ipsum is not simply random text. It has roots in a piece of classical Latin literature from 45 BC, making it over 2000 years old. Alden Marsh, a Latin professor at Harlow Ridge College in Virginia, looked ...</p>
  <p class="testi-name">Standard Chunk</p>
  <p class="testi-role">Busuness Man</p>
</article>
<div class="abs quote-badge" style="left:187px">&ldquo;</div>
<article class="abs testi-card" style="left:611px">
  <p class="body-text">Contrary to popular belief, Lorem Ipsum is not simply random text. It has roots in a piece of classical Latin literature from 45 BC, making it over 2000 years old. Alden Marsh, a Latin professor at Harlow Ridge College in Virginia, looked ...</p>
  <p class="testi-name">Finibus Bonorum</p>
  <p class="testi-role">Busuness Man</p>
</article>
<div class="abs quote-badge" style="left:642px">&ldquo;</div>

<section class="abs contact" role="img" aria-label="Photo of a garden with palm trees and a pool at sunset"></section>
<h2 class="abs contact-title">Send a Message</h2>
<p class="abs contact-sub">There are many variations of passages of Lorem</p>
<div class="abs field" style="top:2600px">Name</div>
<div class="abs field" style="top:2646px">Email</div>
<div class="abs field" style="top:2694px">Phone</div>
<div class="abs field field-msg">Message ...</div>
<div class="abs btn-gold send-btn">SEND</div>

<footer class="abs footer"></footer>
<span class="abs footer-mark"></span>
<p class="abs footer-name">Brackwell</p>
<p class="abs footer-call"><b>Call Us:</b> 555-204-7731, <b>E.</b> info@brackwell.com.com</p>
<span class="abs f-social" style="left:507px"><i></i></span>
<span class="abs f-social filled" style="left:555px"><i></i></span>
<span class="abs f-social" style="left:603px"><i></i></span>
<span class="abs f-social" style="left:651px"><i></i></span>
<p class="abs copyright">&copy; 2018 BRACKWELL CONSTRUCTIONS. ALL RIGHTS RESERVED.</p>
<p class="abs legal">Terms &amp; Conditions &nbsp;|&nbsp; Privacy Policy</p>

</body>
</html>
```